We need a poster designed for use on facebook, as well as to print out for advertising in local noticeboards and shop windows.
The poster will advertise the Tallowbrook Turf Club 30th Anniversary Ball.
the ball will be held on the 28th April 2018 at the Tallowbrook Community Hall.
Time will be 630pm till late. Ticket Price is $120 which includes 3 course dinner, drinks on arrival and entertainment during the evening.
Additional details will need to be added to the poster at a later date.
The tallowbrook Turf Club is a horse racing club run by the community. The club has been incorporateds for 30 years. This Ball will be a celebration of that anniversary.

Target Market(s)

Middlemount Community

Industry/Entity Type

Club

Font styles to use
Serif
Decorative

Colors
1b1b1b
fbfbfb
6b449b
886aae
a64599
ffc214

Requirements
Must have
• Include
• where when time and cost
• ticket inclusions
• entertainement by Colin Verity
Nice to have
• Attached are some images for inspiration.
• It would be nice to have the race club logo included somewhere however not prominant.
Should not have
• Abstract geometriic lines
• images of people
• primary colours

```html
<!DOCTYPE html>
<html lang="en">
<head>
<meta charset="utf-8">
<title>Tallowbrook Turf Clubs 30th Anniversary Ball</title>
<link rel="stylesheet" href="https://fonts.googleapis.com/css2?family=Cinzel:wght@400;500&family=Cormorant+Garamond:wght@500;600&family=Great+Vibes&display=swap">
<style>
  :root {
    --page-bg: #cfcfcf;
    --poster-dark: #0c1616;
    --poster-mid: #1a2a2a;
    --ink-light: #fbfbfb;
    --gold-light: #fff1b0;
    --gold: #ffc214;
    --gold-deep: #b8860b;
    --gold-dark: #7a5a08;
    --banner-white: #fbfbfb;
    --club-ink: #1b1b1b;
  }
  * { margin: 0; padding: 0; box-sizing: border-box; }
  html, body { width: 1200px; height: 880px; overflow: hidden; background: var(--page-bg); }

  .poster {
    position: absolute; left: 289px; top: 0; width: 622px; height: 880px;
    background: radial-gradient(ellipse at 50% 40%, var(--poster-mid) 0%, var(--poster-dark) 75%);
    color: var(--ink-light); overflow: hidden;
  }

  .gold-text {
    background: linear-gradient(180deg, var(--gold-light) 0%, var(--gold) 40%, var(--gold-deep) 75%, var(--gold-light) 100%);
    -webkit-background-clip: text; background-clip: text; color: transparent;
  }

  .club-banner {
    position: absolute; left: 40px; top: 0; width: 168px; height: 172px;
    background: var(--banner-white);
    border: 3px solid var(--gold-deep); border-top: none;
    clip-path: polygon(0 0, 100% 0, 100% 100%, 50% 88%, 0 100%);
    display: flex; flex-direction: column; align-items: center; justify-content: center; gap: 8px;
    padding-bottom: 16px;
  }
  .club-banner .club-dot { width: 14px; height: 14px; border-radius: 50%; background: var(--club-ink); }
  .club-banner .club-name {
    font-family: 'Cinzel', serif; font-weight: 500; font-size: 17px; line-height: 1.2;
    color: var(--club-ink); text-align: center;
  }

  .club-title {
    position: absolute; left: 230px; top: 42px; width: 364px; text-align: center;
    font-family: 'Cinzel', serif; font-weight: 400; font-size: 44px; line-height: 48px;
    letter-spacing: 2px; padding: 8px 0;
    border-top: 2px solid var(--gold-deep); border-bottom: 2px solid var(--gold-deep);
  }

  .anniversary-ornament {
    position: absolute; left: 85px; top: 180px; width: 453px; height: 210px;
    background: radial-gradient(ellipse at center, rgba(255,194,20,0.35) 0%, rgba(184,134,11,0.18) 45%, rgba(12,22,22,0) 72%);
  }
  .anniversary-number {
    position: absolute; left: 0; width: 622px; top: 232px; text-align: center;
    font-family: 'Cormorant Garamond', serif; font-weight: 600; font-size: 118px; line-height: 110px;
  }
  .anniversary-number sup { font-size: 22px; vertical-align: 62px; margin-left: 2px; }

  .event-title {
    position: absolute; left: 0; width: 622px; top: 385px; text-align: center;
    font-family: 'Great Vibes', cursive; font-size: 112px; line-height: 96px;
  }
  .event-title span { display: block; }
  .event-title .second-line { padding-right: 70px; }

  .star-row { position: absolute; left: 245px; top: 600px; width: 132px; height: 30px; }

  .when-block {
    position: absolute; left: 50px; top: 656px; width: 290px; height: 100px;
    font-family: 'Cinzel', serif; color: var(--ink-light);
  }
  .date { position: absolute; left: 0; width: 130px; text-align: center; }
  .date .month { font-size: 24px; line-height: 26px; }
  .date .day { font-size: 50px; line-height: 46px; font-weight: 500; }
  .date .year { font-size: 26px; line-height: 26px; letter-spacing: 2px; }
  .when-divider { position: absolute; left: 145px; top: 2px; width: 2px; height: 96px; background: var(--gold-deep); }
  .time { position: absolute; left: 160px; width: 130px; text-align: center; }
  .time .start { font-size: 26px; line-height: 34px; }
  .time .till { font-size: 11px; line-height: 18px; letter-spacing: 1px; }
  .time .till::before, .time .till::after { content: ""; display: inline-block; width: 20px; height: 1px; background: var(--ink-light); vertical-align: middle; margin: 0 7px; }
  .time .end { font-size: 36px; line-height: 40px; }

  .venue {
    position: absolute; left: 65px; top: 773px; width: 247px;
    border-top: 2px solid var(--gold-deep); padding-top: 10px;
    font-family: 'Cinzel', serif; font-size: 25px; line-height: 30px; text-align: center;
    white-space: nowrap; display: flex; flex-direction: column; align-items: center;
  }

  .ticket-seal {
    position: absolute; left: 349px; top: 616px; width: 230px; height: 230px; border-radius: 50%;
    background: radial-gradient(circle at 40% 30%, var(--gold-light) 0%, var(--gold) 38%, var(--gold-deep) 80%, var(--gold-dark) 100%);
    box-shadow: 0 0 22px rgba(255,194,20,0.35);
    color: var(--club-ink); text-align: center; font-family: 'Cinzel', serif;
    display: flex; flex-direction: column; align-items: center; padding-top: 14px;
  }
  .ticket-seal .seal-stars { font-size: 11px; letter-spacing: 4px; line-height: 14px; }
  .ticket-seal .label { font-size: 16px; line-height: 20px; }
  .ticket-seal .price { font-family: 'Cormorant Garamond', serif; font-weight: 600; font-size: 86px; line-height: 78px; letter-spacing: -2px; }
  .ticket-seal .price sup { font-size: 36px; vertical-align: 30px; }
  .ticket-seal .includes { font-size: 12px; line-height: 16px; margin-top: 2px; }
  .ticket-seal .inclusions { font-size: 10px; line-height: 12px; }
  .ticket-seal .entertainer { font-family: 'Great Vibes', cursive; font-size: 22px; line-height: 22px; }
</style>
</head>
<body>
  <main class="poster">
    <div class="club-banner">
      <span class="club-dot"></span>
      <span class="club-name">Tallowbrook<br>Turf Club</span>
    </div>

    <h1 class="club-title">Tallowbrook<br>Turf Clubs</h1>

    <div class="anniversary-ornament" role="img" aria-label="Gold filigree scroll ornament framing the anniversary number"></div>
    <div class="anniversary-number gold-text">30<sup>TH</sup></div>

    <h2 class="event-title gold-text"><span>Anniversary</span><span class="second-line">Ball</span></h2>

    <svg class="star-row" viewBox="0 0 132 30" aria-hidden="true">
      <defs>
        <linearGradient id="starGold" x1="0" y1="0" x2="0" y2="1">
          <stop offset="0" stop-color="#fff1b0"/><stop offset="1" stop-color="#ffc214"/>
        </linearGradient>
        <polygon id="star" points="0,-10 2.35,-3.2 9.5,-3.1 3.8,1.2 5.9,8.1 0,4 -5.9,8.1 -3.8,1.2 -9.5,-3.1 -2.35,-3.2"/>
      </defs>
      <g fill="url(#starGold)">
        <use href="#star" transform="translate(10,11) scale(0.8)"/>
        <use href="#star" transform="translate(37,17) scale(0.95)"/>
        <use href="#star" transform="translate(66,17) scale(1.25)"/>
        <use href="#star" transform="translate(95,17) scale(0.95)"/>
        <use href="#star" transform="translate(122,11) scale(0.8)"/>
      </g>
    </svg>

    <section class="when-block">
      <div class="date">
        <div class="month">April</div>
        <div class="day">28</div>
        <div class="year">2018</div>
      </div>
      <div class="when-divider"></div>
      <div class="time">
        <div class="start">6:30PM</div>
        <div class="till">TILL</div>
        <div class="end">LATE</div>
      </div>
    </section>

    <div class="venue"><span>Tallowbrook</span><span>Community Hall</span></div>

    <section class="ticket-seal">
      <div class="seal-stars">★★★</div>
      <div class="label">TICKET PRICE</div>
      <div class="price"><sup>$</sup>120</div>
      <div class="includes">INCLUDES</div>
      <div class="inclusions">3 COURSE DINNER<br>DRINKS ON ARRIVAL<br>ENTERTAINMENT BY</div>
      <div class="entertainer">Colin Verity</div>
      <div class="seal-stars">★★★</div>
    </section>
  </main>
</body>
</html>
```